" A Vendaluz Store comercializa produtos nos seguintes segmentos: automotivo, cine e foto, componentes, cuidados pessoais, eletrodomésticos e eletroportáteis, eletrônicos, games, informatica, instrumentos musicais, materiais elétricos, som profissional e telefonia além de produtos de decoração. Tem como objetivo fornecer produtos de excelência e proporcionar uma marcante experiência de compra na modalidade e-commerce. "

```html
<!DOCTYPE html>
<html lang="pt-BR">
<head>
<meta charset="UTF-8">
<title>Vendaluz Store – Assinatura de e-mail</title>
<link rel="stylesheet" href="https://fonts.googleapis.com/css2?family=Montserrat:wght@400;500;600&display=swap">
<style>
  :root {
    --page-bg: #f2f2f2;
    --ink-dark: #121a22;
    --gold: #c9a24a;
    --gold-light: #e2c57a;
    --card-white: #ffffff;
    --text-grey: #6b6b6b;
    --line-grey: #d6d6d6;
  }
  * { box-sizing: border-box; margin: 0; padding: 0; }
  html, body {
    width: 1200px; height: 1200px; overflow: hidden;
    background: var(--page-bg);
    font-family: "Montserrat", Arial, sans-serif;
  }
  .signature {
    position: absolute;
    left: 50px; top: 490px;
    width: 1100px; height: 220px;
    box-shadow: 0 6px 24px rgba(0,0,0,0.08);
    border-radius: 0 60px 0 0;
    overflow: hidden;
  }
  .signature-shapes { position: absolute; inset: 0; }
  .brand {
    position: absolute; left: 60px; top: 0; height: 220px;
    display: flex; align-items: center; gap: 16px;
  }
  .brand-square {
    width: 22px; height: 22px; background: var(--gold); flex: none;
  }
  .brand-name {
    color: var(--gold);
    font-weight: 600; font-size: 27px; letter-spacing: 2px;
    text-transform: uppercase; white-space: nowrap;
  }
  .person {
    position: absolute; left: 565px; top: 76px;
    white-space: nowrap;
  }
  .person-name {
    color: var(--gold); font-weight: 500; font-size: 31px; line-height: 1.1;
  }
  .person-role {
    color: var(--text-grey); font-size: 17px; margin-top: 6px;
  }
  .contacts {
    position: absolute; left: 880px; top: 36px;
    padding-left: 20px; border-left: 2px solid var(--line-grey);
    list-style: none;
  }
  .contact {
    display: flex; align-items: center; gap: 10px;
    font-size: 13px; color: var(--text-grey); height: 29px;
    white-space: nowrap;
  }
  .contact-icon {
    width: 20px; height: 20px; border-radius: 50%;
    background: var(--ink-dark);
    display: flex; align-items: center; justify-content: center; flex: none;
  }
  .contact-icon svg { width: 11px; height: 11px; }
</style>
</head>
<body>
  <section class="signature" aria-label="Assinatura de e-mail Vendaluz Store">
    <svg class="signature-shapes" viewBox="0 0 1100 220" preserveAspectRatio="none" aria-hidden="true">
      <defs>
        <linearGradient id="goldBand" x1="0" y1="0" x2="1" y2="1">
          <stop offset="0" stop-color="#e2c57a"/>
          <stop offset="1" stop-color="#c9a24a"/>
        </linearGradient>
      </defs>
      <rect width="1100" height="220" fill="#ffffff"/>
      <polygon points="480,0 540,0 480,220 420,220" fill="url(#goldBand)"/>
      <polygon points="0,0 500,0 440,220 0,220" fill="#121a22"/>
      <rect x="440" y="212" width="660" height="8" fill="url(#goldBand)"/>
    </svg>

    <div class="brand">
      <span class="brand-square"></span>
      <span class="brand-name">Vendaluz Store</span>
    </div>

    <div class="person">
      <p class="person-name">Nome Sobrenome</p>
      <p class="person-role">Co. Founder</p>
    </div>

    <ul class="contacts">
      <li class="contact">
        <span class="contact-icon"><svg viewBox="0 0 24 24"><path fill="#fff" d="M6.6 10.8a15.1 15.1 0 0 0 6.6 6.6l2.2-2.2a1 1 0 0 1 1-.25 11.4 11.4 0 0 0 3.6.57 1 1 0 0 1 1 1V20a1 1 0 0 1-1 1A17 17 0 0 1 3 4a1 1 0 0 1 1-1h3.5a1 1 0 0 1 1 1c0 1.25.2 2.45.57 3.57a1 1 0 0 1-.25 1z"/></svg></span>
        +55 11 4000-2020
      </li>
      <li class="contact">
        <span class="contact-icon"><svg viewBox="0 0 24 24"><path fill="#fff" d="M12 2a7 7 0 0 0-7 7c0 5.25 7 13 7 13s7-7.75 7-13a7 7 0 0 0-7-7zm0 9.5A2.5 2.5 0 1 1 12 6.5a2.5 2.5 0 0 1 0 5z"/></svg></span>
        R. das Palmeiras, 120
      </li>
      <li class="contact">
        <span class="contact-icon"><svg viewBox="0 0 24 24"><path fill="#fff" d="M12 2a7 7 0 0 0-7 7c0 5.25 7 13 7 13s7-7.75 7-13a7 7 0 0 0-7-7zm0 9.5A2.5 2.5 0 1 1 12 6.5a2.5 2.5 0 0 1 0 5z"/></svg></span>
        Centro, São Paulo, SP
      </li>
      <li class="contact">
        <span class="contact-icon"><svg viewBox="0 0 24 24"><path fill="#fff" d="M3 5h18v14H3zm2 2v.5l7 4.5 7-4.5V7l-7 4.5z"/></svg></span>
        contato@vendaluz.com
      </li>
      <li class="contact">
        <span class="contact-icon"><svg viewBox="0 0 24 24"><circle cx="12" cy="12" r="8" fill="none" stroke="#fff" stroke-width="2"/><path d="M4 12h16M12 4c3 3 3 13 0 16M12 4c-3 3-3 13 0 16" fill="none" stroke="#fff" stroke-width="1.6"/></svg></span>
        www.vendaluz.com
      </li>
    </ul>
  </section>
</body>
</html>
```